Kestrel Bridge Consulting (KBC) Business Card Design

I would like to create double-sided business cards that contain:
1) Name: Derek Molvane
2) Phone Number: +1 (555) 218-4907
3) Email: Derek.Molvane@KestrelBridgeConsulting.example
4) Website: KestrelBridgeConsulting.example

I would like to include my logo and a color scheme similar to the Varnholt Grand Prix Ostera squad color scheme (black, silver, greenish-blue – but can also include regular blue)

What we do: Our company develops and delivers innovative and pragmatic information technology and cybersecurity risk and compliance solutions for organizations in the commercial market as well as the federal, and state/local sectors.

```html
<!DOCTYPE html>
<html lang="en">
<head>
<meta charset="utf-8">
<title>Kestrel Bridge Consulting – Business Card</title>
<link rel="stylesheet" href="https://fonts.googleapis.com/css2?family=Michroma&family=Quicksand:wght@400;500;700&display=swap">
<style>
  :root {
    --backdrop: #e7e5e1;
    --navy-deep: #07152b;
    --navy: #0d2142;
    --ink: #05070c;
    --silver: #eef1f5;
    --teal: #1fa7b8;
    --blue: #1b84d6;
    --glow: #2fb8e8;
    --rule: #1a9c9c;
  }
  * { margin: 0; padding: 0; box-sizing: border-box; }
  html, body { width: 1200px; height: 900px; overflow: hidden; }
  body {
    background: var(--backdrop);
    display: flex;
    flex-direction: column;
    align-items: center;
    justify-content: center;
    gap: 40px;
    font-family: "Quicksand", sans-serif;
  }
  .card {
    position: relative;
    width: 700px;
    height: 400px;
    border-radius: 36px;
    overflow: hidden;
    box-shadow: 0 14px 30px rgba(0,0,0,0.25);
  }
  .card--front {
    background: linear-gradient(160deg, var(--navy) 0%, var(--navy-deep) 100%);
  }
  .card--back {
    background: linear-gradient(145deg, var(--ink) 0%, #070d18 55%, var(--navy) 100%);
  }
  .network-texture {
    position: absolute;
    top: 0;
    right: 0;
    width: 360px;
    height: 240px;
    background:
      radial-gradient(circle at 88% 6%, rgba(47,184,232,0.55) 0%, rgba(47,184,232,0) 18%),
      radial-gradient(ellipse at 85% 15%, rgba(27,132,214,0.28) 0%, rgba(27,132,214,0) 65%);
  }
  .wordmark {
    display: flex;
    align-items: center;
    gap: 14px;
  }
  .wordmark__dot {
    width: 16px;
    height: 16px;
    border-radius: 50%;
    background: var(--teal);
  }
  .wordmark__name {
    font-family: "Michroma", sans-serif;
    color: var(--silver);
    text-transform: uppercase;
    line-height: 1.18;
    border-left: 1px solid rgba(238,241,245,0.6);
    padding-left: 14px;
  }
  .card--front .wordmark {
    position: absolute;
    left: 150px;
    top: 145px;
  }
  .card--front .wordmark__name { font-size: 26px; }
  .card--back .wordmark {
    position: absolute;
    left: 40px;
    top: 42px;
  }
  .card--back .wordmark__name { font-size: 19px; }
  .contact {
    position: absolute;
    left: 40px;
    right: 40px;
    bottom: 36px;
    color: var(--silver);
  }
  .contact__name-row {
    display: flex;
    align-items: center;
    gap: 14px;
    margin-bottom: 6px;
  }
  .contact__name {
    font-family: "Michroma", sans-serif;
    font-size: 20px;
    color: var(--blue);
    text-transform: uppercase;
    white-space: nowrap;
  }
  .contact__rule {
    flex: 1;
    height: 1px;
    background: var(--rule);
  }
  .contact__line {
    font-size: 13.5px;
    font-weight: 500;
    letter-spacing: 0.2px;
    line-height: 1.7;
    white-space: nowrap;
  }
  .contact__sep { color: var(--teal); padding: 0 6px; }
</style>
</head>
<body>
  <section class="card card--front">
    <div class="network-texture" role="img" aria-label="Faint glowing network of connected nodes in blue"></div>
    <div class="wordmark">
      <span class="wordmark__dot"></span>
      <span class="wordmark__name">Kestrel<br>Bridge<br>Consulting</span>
    </div>
  </section>

  <section class="card card--back">
    <div class="network-texture" role="img" aria-label="Faint glowing network of connected nodes in blue"></div>
    <div class="wordmark">
      <span class="wordmark__dot"></span>
      <span class="wordmark__name">Kestrel<br>Bridge<br>Consulting</span>
    </div>
    <div class="contact">
      <div class="contact__name-row">
        <span class="contact__name">Derek Molvane</span>
        <span class="contact__rule"></span>
      </div>
      <p class="contact__line">+1 (555) 218-4907</p>
      <p class="contact__line">KestrelBridgeConsulting.example<span class="contact__sep">|</span>Derek.Molvane@KestrelBridgeConsulting.example</p>
    </div>
  </section>
</body>
</html>
```